International gym review site. Needs a full website frontend (mobile + desktop) designing and a logo

Our UK based business 'LiftHarbor' is launching its international review website for independent and hotel gyms. Our website will be a fresh, funky and clean version of Wanderquill but for gyms.
We require the designs in sketch, psd, illustrator

We would like to see clean designs that incorporate gym style icons. We also require our logo designing which will need to complement the design of the site. We have included wireframes of how we envisage the site coming together. However, we are very flexible on this and have nothing set in stone.

We would like the designs to mobile first focused with desktop experince being the latter (although we have wireframed for desktop - we are very open to ideas and suggestions)

Please find below a number of websites that we like and have found inspiration from:

- https://www.bookvane.example/uk/
- chatterloom.example
- Map is cool on here https://bigroster.bypilotcraft.example/
- Looks cool like nest n'go (listing section could be smaller) -https://tintforge.example/demos/themes/?product=rowable
- Like this but needs to be more compact https://rowkit-demos.brimfold.example/rentals/listing/private-bedroom-w-bathroom/
- Like the homepage of this one https://rankhop.venmora.example/
- https://www.paddlo.example.co.uk/hotels - looks clean, like the layout of this especially the hotel section
- https://www.paddlo.example.co.uk/Barcelona-Hotels.48213.hotel.ksp - the good to know section is good
- https://chipwire.example/2017/10/20/flickcast-unveils-a-suite-of-new-tools-to-help-creators-grow-their-channels-and-make-money/
- https://www.quietlodging.example/
- https://www.wheelmarket.example.co.uk

Target Market(s)

Fitness users and hotel goers who want to use a gym. Generally affluent aged 20-50years old of multi-nationalities

Industry/Entity Type

Fitness

Logo Text

LiftHarbor (optional)

Number of Pages Required

5+ page

Colors

Designer to choose colors to be used in the design.

Requirements
Must have
• Clean, flat minimal, pleasing on the eye.
• Bright / colourful
• Clean fonts (no specific font picked, will leave colour palette and fonts to the designer)
Should not have
• Cluttered and disorganised feel.
• Dark and dreary.

```html
<!DOCTYPE html>
<html lang="en">
<head>
<meta charset="utf-8">
<title>LiftHarbor — Gym Reviews</title>
<link rel="stylesheet" href="https://fonts.googleapis.com/css2?family=Montserrat:wght@600;700;800;900&family=Open+Sans:wght@400;600;700&display=swap">
<style>
:root{
  --blue:#1479ee;
  --blue-dark:#0f66d0;
  --ink:#1d1d1d;
  --grey:#8a8a8a;
  --line:#bdbdbd;
  --white:#fff;
  --footer:#1b1b1b;
  --field:#262626;
  --footer-text:#cfcfcf;
}
*{box-sizing:border-box;margin:0;padding:0}
html,body{width:1200px;height:2853px;overflow:hidden;background:var(--white)}
body{font-family:"Open Sans",Arial,sans-serif;color:var(--ink);position:relative}
.wrap{width:702px;margin:0 auto;position:relative}
.heading{font-family:"Montserrat",Arial,sans-serif;font-weight:900;text-transform:uppercase}

/* header */
.site-header{position:absolute;top:0;left:0;width:1200px;height:106px;background:var(--blue);z-index:3}
.brand-panel{position:absolute;left:0;top:0;width:400px;height:106px;background:var(--white);clip-path:polygon(0 0,100% 0,345px 100%,0 100%)}
.brand{position:absolute;left:250px;top:38px;display:flex;align-items:center;gap:8px;font-family:"Montserrat",sans-serif;font-weight:800;font-size:17px;color:var(--ink)}
.brand-mark{width:14px;height:14px;background:var(--ink)}
.topbar{position:absolute;top:16px;left:624px;display:flex;font-size:9px;color:var(--white);font-weight:600}
.topbar span{margin-right:40px}
.topbar .active{text-decoration:underline}
.account{position:absolute;top:16px;left:782px;font-size:9px;color:var(--white)}
.main-nav{position:absolute;top:62px;left:420px;display:flex;gap:0;font-size:11px;color:var(--white)}
.main-nav a{color:inherit;text-decoration:none;margin-right:24px}
.main-nav .current{font-weight:700}
.search{position:absolute;top:55px;left:833px;width:118px;height:29px;background:var(--blue-dark);color:var(--white);font-size:10px;padding:8px 12px;display:flex;justify-content:space-between;align-items:center}

/* hero */
.hero{position:absolute;top:106px;left:0;width:1200px;height:379px;background:linear-gradient(115deg,#8d959b 0%,#79848c 40%,#5c6f80 75%,#4b6379 100%)}
.hero-card{position:absolute;left:428px;top:116px;width:344px;height:196px;background:var(--white);text-align:center;padding-top:76px;box-shadow:0 2px 8px rgba(0,0,0,.15)}
.hero-badge{position:absolute;left:549px;top:57px;width:104px;height:104px;border-radius:50%;background:var(--white);z-index:2;box-shadow:0 1px 6px rgba(0,0,0,.2);display:flex;align-items:center;justify-content:center;font-family:"Montserrat",sans-serif;font-weight:800;font-size:11px;color:var(--ink)}
.hero-card h1{font-family:"Montserrat",sans-serif;font-weight:800;font-size:12px}
.stars{color:#9a9a9a;font-size:12px;letter-spacing:2px;margin:6px 0 8px}
.hero-card p{font-size:10.5px;line-height:18px;color:var(--grey);padding:0 22px}

/* listings */
.listing{position:absolute;left:0;width:1200px}
.section-title{font-size:19px;letter-spacing:.3px;height:29px}
.cards{display:flex;gap:11px}
.card{width:227px}
.card-photo{height:200px}
.card h3{font-family:"Montserrat",sans-serif;font-weight:800;font-size:12px;margin-top:16px}
.card p{font-size:10.5px;line-height:16.5px;color:var(--grey);margin-top:5px;height:66px}
.btn-outline{display:inline-block;width:80px;height:27px;border:1px solid var(--line);font-size:9px;line-height:25px;text-align:center;color:#555;margin-top:15px}
.btn-blue{display:block;width:130px;height:35px;background:var(--blue);color:var(--white);font-family:"Montserrat",sans-serif;font-weight:700;font-size:10px;text-align:center;line-height:35px;margin:40px auto 0}

/* band */
.promo{position:absolute;top:1915px;left:0;width:1200px;height:278px;background:var(--blue);text-align:center;color:var(--white)}
.promo h2{font-family:"Montserrat",sans-serif;font-weight:800;font-size:19px;margin-top:48px}
.promo p{width:620px;margin:18px auto 0;font-size:11.5px;line-height:23.5px}
.btn-white{display:block;width:130px;height:36px;background:var(--white);color:var(--blue);font-size:10px;font-weight:700;line-height:36px;margin:24px auto 0}

/* events */
.events{position:absolute;top:2236px;left:0;width:1200px}
.event-row{display:flex;gap:9px;margin-top:9px}
.event{width:133px}
.event-photo{height:130px}
.event h4{font-family:"Montserrat",sans-serif;font-weight:800;font-size:12px;margin-top:18px}

/* footer */
.site-footer{position:absolute;top:2488px;left:0;width:1200px;height:365px;background:var(--footer);color:var(--footer-text)}
.footer-col{position:absolute;top:44px}
.footer-col h5{font-family:"Montserrat",sans-serif;font-weight:800;font-size:12px;color:var(--white);text-transform:uppercase;margin-bottom:22px}
.info{left:249px;width:200px;font-size:9.5px;line-height:16px}
.info b{color:var(--white);font-weight:700}
.socials{display:flex;gap:5px;margin-top:14px}
.socials span{width:21px;height:21px;background:var(--white)}
.link-list{list-style:none;font-size:9.5px}
.link-list li{margin-bottom:12.5px}
.link-list li::before{content:"›";margin-right:8px}
.col-gym{left:466px}
.col-links{left:633px}
.contact{left:749px;width:202px}
.field{height:27px;background:var(--field);font-size:9px;padding:8px 10px;margin-bottom:13px}
.field.tall{height:71px}
.send{width:82px;height:27px;background:var(--blue);color:var(--white);font-size:9.5px;font-weight:700;text-align:center;line-height:27px}
.legal{position:absolute;left:249px;top:323px;width:702px;border-top:1px solid #2e2e2e;padding-top:14px;font-size:9px}
.legal b{color:var(--white)}
</style>
</head>
<body>

<header class="site-header">
  <div class="brand-panel"></div>
  <div class="brand"><span class="brand-mark"></span>LiftHarbor</div>
  <div class="topbar"><span class="active">$ USD</span><span>€ EUR</span><span>£ GBP</span></div>
  <div class="account">Add Submission &nbsp;&nbsp;/&nbsp;&nbsp; Register &nbsp;&nbsp;/&nbsp;&nbsp; Login</div>
  <nav class="main-nav">
    <a>HOME</a><a>ABOUT US</a><a class="current">HOTEL GYM</a><a>EVENTS</a><a>BLOG</a><a>CONTACT US</a>
  </nav>
  <div class="search">Search...
    <svg width="11" height="11" viewBox="0 0 12 12"><circle cx="5" cy="5" r="3.8" fill="none" stroke="#fff" stroke-width="1.6"/><line x1="8" y1="8" x2="11" y2="11" stroke="#fff" stroke-width="1.6"/></svg>
  </div>
</header>

<section class="hero" role="img" aria-label="Street map of the city with gym locations">
  <div class="hero-badge">LiftHarbor</div>
  <div class="hero-card">
    <h1>LOREM IPSUM IS SIMPLY DUMMY</h1>
    <div class="stars">★★★★★</div>
    <p>Lorem Ipsum is simply dummy text of the printing and typesetting industry. Lorem Ipsum has been the industry's standard dummy text ever since the 1500s.</p>
  </div>
</section>

<section class="listing" style="top:532px">
  <div class="wrap">
    <div class="cards">
      <article class="card"><div class="card-photo" role="img" aria-label="Runner on a treadmill" style="background:linear-gradient(#6d6d6d,#2f2f2f)"></div><h3>LOREM IPSUM IS SIMPLY DUMMY</h3><p>Lorem Ipsum is simply dummy text of the printing and typesetting industry. Lorem Ipsum has been the industry's standard dummy text ever since the 1500s.</p><span class="btn-outline">READ MORE</span></article>
      <article class="card"><div class="card-photo" role="img" aria-label="Woman training on a cross trainer" style="background:linear-gradient(#d9d9d9,#8f8f8f)"></div><h3>LOREM IPSUM IS SIMPLY DUMMY</h3><p>Lorem Ipsum is simply dummy text of the printing and typesetting industry. Lorem Ipsum has been the industry's standard dummy text ever since the 1500s.</p><span class="btn-outline">READ MORE</span></article>
      <article class="card"><div class="card-photo" role="img" aria-label="Athlete training with battle ropes" style="background:linear-gradient(#5a4540,#231d1c)"></div><h3>LOREM IPSUM IS SIMPLY DUMMY</h3><p>Lorem Ipsum is simply dummy text of the printing and typesetting industry. Lorem Ipsum has been the industry's standard dummy text ever since the 1500s.</p><span class="btn-outline">READ MORE</span></article>
    </div>
  </div>
</section>

<section class="listing" style="top:914px">
  <div class="wrap">
    <h2 class="heading section-title">HOTEL GYMS</h2>
    <div class="cards">
      <article class="card"><div class="card-photo" role="img" aria-label="Rack of dumbbells in a hotel gym" style="background:linear-gradient(#a7a7a7,#3c3c3c)"></div><h3>LOREM IPSUM IS SIMPLY DUMMY</h3><p>Lorem Ipsum is simply dummy text of the printing and typesetting industry. Lorem Ipsum has been the industry's standard dummy text ever since the 1500s.</p><span class="btn-outline">READ MORE</span></article>
      <article class="card"><div class="card-photo" role="img" aria-label="Trainer shoe on gym equipment" style="background:linear-gradient(#bcbcbc,#6b6b6b)"></div><h3>LOREM IPSUM IS SIMPLY DUMMY</h3><p>Lorem Ipsum is simply dummy text of the printing and typesetting industry. Lorem Ipsum has been the industry's standard dummy text ever since the 1500s.</p><span class="btn-outline">READ MORE</span></article>
      <article class="card"><div class="card-photo" role="img" aria-label="Two people on exercise bikes" style="background:linear-gradient(#c79484,#6c5a55)"></div><h3>LOREM IPSUM IS SIMPLY DUMMY</h3><p>Lorem Ipsum is simply dummy text of the printing and typesetting industry. Lorem Ipsum has been the industry's standard dummy text ever since the 1500s.</p><span class="btn-outline">READ MORE</span></article>
    </div>
    <span class="btn-blue">VIEW MORE</span>
  </div>
</section>

<section class="listing" style="top:1407px">
  <div class="wrap">
    <h2 class="heading section-title">INDEPENDMENT GYMS</h2>
    <div class="cards">
      <article class="card"><div class="card-photo" role="img" aria-label="Weight plates on a gym floor" style="background:linear-gradient(#5b5b5b,#252525)"></div><h3>LOREM IPSUM IS SIMPLY DUMMY</h3><p>Lorem Ipsum is simply dummy text of the printing and typesetting industry. Lorem Ipsum has been the industry's standard dummy text ever since the 1500s.</p><span class="btn-outline">READ MORE</span></article>
      <article class="card"><div class="card-photo" role="img" aria-label="Step aerobics class" style="background:linear-gradient(#8a8d8c,#6a5234)"></div><h3>LOREM IPSUM IS SIMPLY DUMMY</h3><p>Lorem Ipsum is simply dummy text of the printing and typesetting industry. Lorem Ipsum has been the industry's standard dummy text ever since the 1500s.</p><span class="btn-outline">READ MORE</span></article>
      <article class="card"><div class="card-photo" role="img" aria-label="Runner on a treadmill" style="background:linear-gradient(#6d6d6d,#2f2f2f)"></div><h3>LOREM IPSUM IS SIMPLY DUMMY</h3><p>Lorem Ipsum is simply dummy text of the printing and typesetting industry. Lorem Ipsum has been the industry's standard dummy text ever since the 1500s.</p><span class="btn-outline">READ MORE</span></article>
    </div>
    <span class="btn-blue">VIEW MORE</span>
  </div>
</section>

<section class="promo">
  <h2>LOREM IPSUM IS SIMPLY DUMMY TEXT</h2>
  <p>Lorem Ipsum is simply dummy text of the printing and typesetting industry. Lorem Ipsum has been the industry's standard dummy text ever since the 1500s, when an unknown printer took a galley of type and scrambled it to make a type specimen book. It has survived not only five centuries, but also the leap into electronic typesetting, remaining essentially unchanged.</p>
  <span class="btn-white">VIEW MORE</span>
</section>

<section class="events">
  <div class="wrap">
    <h2 class="heading section-title">EVENTS NEAR BY</h2>
    <div class="event-row">
      <div class="event"><div class="event-photo" role="img" aria-label="Two people on exercise bikes" style="background:linear-gradient(#c79484,#6c5a55)"></div><h4>01 EVENTS</h4></div>
      <div class="event"><div class="event-photo" role="img" aria-label="Runner on a treadmill" style="background:linear-gradient(#6d6d6d,#2f2f2f)"></div><h4>02 EVENTS</h4></div>
      <div class="event"><div class="event-photo" role="img" aria-label="Athlete training with battle ropes" style="background:linear-gradient(#5a4540,#231d1c)"></div><h4>LOREM IPSUM</h4></div>
      <div class="event"><div class="event-photo" role="img" aria-label="Trainer shoe on gym equipment" style="background:linear-gradient(#bcbcbc,#6b6b6b)"></div><h4>LOREM IPSUM</h4></div>
      <div class="event"><div class="event-photo" role="img" aria-label="Rack of dumbbells" style="background:linear-gradient(#a7a7a7,#3c3c3c)"></div><h4>LOREM IPSUM</h4></div>
    </div>
  </div>
</section>

<footer class="site-footer">
  <div class="footer-col info">
    <h5>Information</h5>
    <p>Lorem Ipsum is simply dummy text of the printing and typesetting industry. Lorem Ipsum has been the industry's</p>
    <p style="margin-top:8px"><b>Address</b><br>Lorem Ipsum is simply dummy text of the printing and typesetting industry.</p>
    <p style="margin-top:8px"><b>Phone Number:</b> 000 0000 0000</p>
    <p style="margin-top:8px"><b>Email:</b> info@liftharbor.example</p>
    <div class="socials"><span></span><span></span><span></span><span></span><span></span><span></span></div>
  </div>
  <div class="footer-col col-gym">
    <h5>Independent Gym</h5>
    <ul class="link-list"><li>Kettlebell Power</li><li>Body Power</li><li>Running</li><li>Cycling</li></ul>
  </div>
  <div class="footer-col col-links">
    <h5>Quik Link</h5>
    <ul class="link-list"><li>Home</li><li>About us</li><li>Events</li><li>Testimonials</li><li>Contact us</li></ul>
  </div>
  <div class="footer-col contact">
    <h5>Contact Us</h5>
    <div class="field">Name</div>
    <div class="field">Email</div>
    <div class="field tall">Messages</div>
    <div class="send">SEND</div>
  </div>
  <div class="legal">Copyright © 2018 <b>HARBORLIFT&amp;CO</b> All Right Reserved.</div>
</footer>

</body>
</html>
```